Web design for upcoming direct placement agency

So were looking for a very modern, simple but professional look. We would like to have the site able to translate into 4 different languages- a few idea sites you can reference would be
www.lantomarsh.com **our favorite**
www.brightfenwick.org

We want to ensure the website is tailored to both our clients as well as potential candidates. We want our clients and candidates to understand that we are dedicated to making sure that we want to build relationships with them and that we want to do everything possible to make sure they succeed.

We'd like to steer away from too many up close photos of people. Instead you could try a shadowed view or distant photo that limits the directness.

we have a domain name- www.veltharidgellc.com

We will upload our business plan as well as a sample business proposal so you have an idea of the information we would like to include.

Target Market(s)

Business' looking to outsource their hiring needs for upper level positions such as but not limited to quality engineers, logistics managers, material managers, etc

Industry/Entity Type

Employment Agency

Number of Pages Required

3 page

Font styles to use
Serif
Sans Serif
Script
Other font styles liked:
• Kennedy Sm Caps

Colors
1b1b1b
9d9d9d
e9e9e9
eeeeee
dadada
0255a3
85acd3
474747

Requirements
Must have
• -ability to translate to English, Spanish, German, and Japanese.
• -Our logo
• -A contact us section
• -Resume upload area
Should not have
• -A job search area
• -pricing info

```html
<!DOCTYPE html>
<html lang="en">
<head>
<meta charset="utf-8">
<title>Veltharidge — Direct Placement Agency</title>
<link href="https://fonts.googleapis.com/css2?family=Raleway:wght@300;400;600;700;800&family=Open+Sans:wght@400;600;700&display=swap" rel="stylesheet">
<style>
:root{
  --ink:#1b1b1b;
  --grey:#9d9d9d;
  --light:#e9e9e9;
  --pale:#eeeeee;
  --line:#dadada;
  --blue:#0255a3;
  --sky:#85acd3;
  --charcoal:#474747;
  --white:#ffffff;
}
*{box-sizing:border-box;margin:0;padding:0}
html,body{width:1200px;height:2644px;overflow:hidden;background:var(--white)}
body{font-family:"Open Sans",Arial,sans-serif;color:var(--charcoal);position:relative}
.page{position:relative;width:1200px;height:2644px;overflow:hidden}

/* header */
.site-header{height:88px;display:flex;align-items:center;justify-content:space-between;padding:0 36px;background:var(--white);position:relative;z-index:3}
.brand{display:flex;align-items:center;gap:10px;font-family:"Raleway",sans-serif;font-weight:800;font-size:22px;color:var(--charcoal);letter-spacing:1px;text-transform:uppercase}
.brand-mark{width:20px;height:20px;border-radius:50%;background:var(--blue)}
.main-nav{display:flex;gap:30px;font-size:14px;color:var(--charcoal);margin-right:10px;margin-top:26px}
.langs{position:absolute;right:36px;top:10px;display:flex;gap:6px}
.langs span{width:22px;height:14px;display:block}

/* hero */
.hero{position:relative;height:490px;background:linear-gradient(180deg,#8a8f96 0%,#5d636b 55%,#3f444a 100%)}
.hero-copy{position:absolute;left:0;right:0;top:176px;text-align:center;color:var(--white)}
.hero-title{font-family:"Raleway",sans-serif;font-weight:800;font-size:44px;letter-spacing:2px;line-height:1.2}
.hero-sub{font-family:"Raleway",sans-serif;font-weight:600;font-size:24px;letter-spacing:1px;margin-top:4px}
.hero-actions{display:flex;justify-content:center;gap:18px;margin-top:26px}
.btn{display:inline-block;font-weight:600;font-size:12px;text-transform:uppercase;padding:11px 22px;border-radius:20px}
.btn-blue{background:var(--blue);color:var(--white)}
.btn-dark{background:var(--charcoal);color:var(--white)}

/* intro */
.intro{position:relative;height:300px;background:var(--white);z-index:2;clip-path:polygon(0 0,100% 0,100% 88%,94% 100%,6% 100%,0 88%);display:flex;padding:66px 0 0 152px}
.intro-title{font-family:"Raleway",sans-serif;font-weight:600;font-size:44px;line-height:1.15;color:var(--blue);width:330px}
.intro-text{width:500px;margin-left:58px;font-size:12px;line-height:1.7;color:var(--charcoal)}
.intro-text p+p{margin-top:14px}

/* clients */
.clients{position:relative;height:380px;margin-top:-40px;padding-top:110px;background:linear-gradient(180deg,#3a3d42,#23262a)}
.section-title{font-family:"Raleway",sans-serif;font-weight:400;font-size:34px;text-align:center;line-height:1.2}
.clients .section-title{color:var(--white)}
.client-row{display:flex;justify-content:center;gap:18px;margin-top:38px}
.client{width:172px;height:92px;background:var(--white);display:flex;align-items:center;justify-content:center;gap:8px;font-family:"Raleway",sans-serif;font-weight:700;font-size:18px;color:var(--charcoal)}
.client i{width:12px;height:12px;background:var(--charcoal);display:block}

/* resume upload */
.upload{position:relative;height:700px;background:var(--light);padding-top:56px;clip-path:polygon(4% 0,96% 0,100% 5%,100% 100%,0 100%,0 5%)}
.upload .section-title{color:var(--blue)}
.upload-lead{text-align:center;font-size:13px;color:var(--charcoal);margin-top:10px}
.upload-form{width:800px;margin:34px auto 0;background:var(--white);border:1px solid var(--line);padding:30px}
.field-row{display:flex;gap:14px;margin-bottom:14px}
.field{flex:1;height:38px;background:var(--white);border:1px solid var(--line);font-size:12px;color:var(--grey);padding:11px 12px}
.dropzone{height:200px;border:2px dashed var(--sky);background:#f7f9fc;display:flex;flex-direction:column;align-items:center;justify-content:center;gap:12px;font-size:13px;color:var(--charcoal)}
.dropzone small{font-size:11px;color:var(--grey)}
.form-foot{display:flex;justify-content:flex-end;margin-top:18px}
.submit{background:var(--blue);color:var(--white);font-weight:600;font-size:12px;text-transform:uppercase;padding:11px 26px;border-radius:2px}

/* goals */
.goals{position:relative;height:390px;background:var(--pale);display:flex;padding:40px 0 0 240px}
.goals-photo{width:290px;height:270px;background:linear-gradient(160deg,#c9ccd1,#7d848d)}
.goals-body{margin-left:52px;width:460px}
.goals-body h2{font-family:"Raleway",sans-serif;font-weight:400;font-size:34px;line-height:1.2;color:var(--blue);margin-bottom:22px}
.goals-body li{list-style:none;display:flex;gap:10px;font-size:12px;line-height:1.4;margin-bottom:14px;color:var(--charcoal)}
.goals-body li i{flex:none;width:8px;height:8px;background:var(--blue);border-radius:50%;margin-top:5px}

/* contact */
.contact{position:relative;height:220px;background:linear-gradient(180deg,#dcdcdc,#cfd1d3)}
.pin{position:absolute;left:580px;top:12px}
.contact-card{position:absolute;left:630px;top:0;width:200px;height:220px;background:var(--white);padding:18px 22px;font-size:11px;line-height:1.7;color:var(--charcoal)}
.contact-card h3{font-family:"Raleway",sans-serif;font-weight:600;font-size:18px;color:var(--ink);margin-bottom:8px}

/* footer */
.site-footer{height:116px;background:var(--white);text-align:center;padding-top:26px}
.foot-nav{display:flex;justify-content:center;gap:26px;font-size:12px;color:var(--charcoal)}
.social{display:flex;justify-content:center;gap:10px;margin-top:12px}
.social span{width:14px;height:14px;border-radius:50%;background:var(--grey);display:block}
.copy{font-size:10px;color:var(--grey);margin-top:12px}
</style>
</head>
<body>
<div class="page">

  <header class="site-header">
    <div class="brand"><span class="brand-mark"></span>Veltharidge</div>
    <nav class="main-nav">
      <span>Home</span><span>Job</span><span>Work with us</span><span>About Us</span><span>Blog</span><span>Career</span><span>Contact Us</span>
    </nav>
    <div class="langs" aria-label="Languages">
      <span style="background:linear-gradient(#1f3c8a 0 50%,#c8102e 50%)" title="English"></span>
      <span style="background:linear-gradient(#c60b1e 0 25%,#ffc400 25% 75%,#c60b1e 75%)" title="Español"></span>
      <span style="background:linear-gradient(#000 0 33%,#dd0000 33% 66%,#ffce00 66%)" title="Deutsch"></span>
      <span style="background:radial-gradient(circle,#bc002d 0 4px,#fff 4.5px)" title="日本語"></span>
    </div>
  </header>

  <section class="hero" role="img" aria-label="Photo of a team of business professionals in suits">
    <div class="hero-copy">
      <div class="hero-title">VELTHARIDGE</div>
      <div class="hero-sub">A NEW APPROACH TO RECRUITING</div>
      <div class="hero-actions">
        <span class="btn btn-blue">Work With Us</span>
        <span class="btn btn-dark">Submit a CV</span>
      </div>
    </div>
  </section>

  <section class="intro">
    <h1 class="intro-title">We are a direct placement agency.</h1>
    <div class="intro-text">
      <p>We partner with businesses to fill upper level positions with people who fit. From quality engineers to logistics and material managers, we search, screen and present only candidates who match your culture, your goals and your pace of growth.</p>
      <p>Our work does not end at the offer letter. We build lasting relationships with clients and candidates alike, staying in touch after placement and doing everything possible to make sure both sides succeed together for years to come.</p>
    </div>
  </section>

  <section class="clients" role="img" aria-label="Blurred photo of a busy crowd of commuters">
    <h2 class="section-title">Our Clients</h2>
    <div class="client-row">
      <div class="client"><i></i>Orbitrail</div>
      <div class="client">Kestrel</div>
      <div class="client">Harborfield</div>
      <div class="client"><i></i>Alder House</div>
      <div class="client">Vantor</div>
    </div>
  </section>

  <section class="upload">
    <h2 class="section-title">Submit Your CV</h2>
    <p class="upload-lead">Send us your resume and we will match you with the right role.</p>
    <div class="upload-form">
      <div class="field-row">
        <div class="field">Full Name</div>
        <div class="field">Email Address</div>
      </div>
      <div class="field-row">
        <div class="field">Phone</div>
        <div class="field">Position of Interest</div>
      </div>
      <div class="dropzone">
        <svg width="34" height="34" viewBox="0 0 34 34" aria-hidden="true">
          <path d="M17 24V6M10 13l7-7 7 7" fill="none" stroke="#0255a3" stroke-width="2.5" stroke-linecap="round" stroke-linejoin="round"/>
          <path d="M5 22v6h24v-6" fill="none" stroke="#0255a3" stroke-width="2.5" stroke-linecap="round" stroke-linejoin="round"/>
        </svg>
        <span>Drop your resume here or browse files</span>
        <small>PDF, DOC or DOCX, up to 5 MB</small>
      </div>
      <div class="form-foot"><span class="submit">Upload Resume</span></div>
    </div>
  </section>

  <section class="goals">
    <div class="goals-photo" role="img" aria-label="Photo of a business team gathered around a laptop"></div>
    <div class="goals-body">
      <h2>Goals</h2>
      <ul>
        <li><i></i>Recruit and secure top talent for our customers</li>
        <li><i></i>Support professional relationships with staff of our customers</li>
        <li><i></i>Ensure we are well aware of the requirements of each of our customers</li>
        <li><i></i>Have front candidates for the position to be filled</li>
        <li><i></i>Provide outstanding customer service</li>
        <li><i></i>Ensure we meet the needs of each and every one of our customers</li>
      </ul>
    </div>
  </section>

  <section class="contact" role="img" aria-label="Street map showing the office location">
    <svg class="pin" width="28" height="38" viewBox="0 0 28 38" aria-hidden="true">
      <path d="M14 0C6.3 0 0 6.1 0 13.7 0 24 14 38 14 38s14-14 14-24.3C28 6.1 21.7 0 14 0z" fill="#2a9d8f"/>
      <circle cx="14" cy="13.5" r="5" fill="#fff"/>
    </svg>
    <div class="contact-card">
      <h3>Contact Us</h3>
      <div>contact@veltharidgellc.com</div>
      <div>4820 Fenmore Road</div>
      <div>Alder Springs</div>
      <div>OR 97410</div>
      <div>+1 555 014 2290</div>
    </div>
  </section>

  <footer class="site-footer">
    <nav class="foot-nav">
      <span>Home</span><span>Job</span><span>Work with us</span><span>About Us</span><span>Blog</span><span>Career</span><span>Contact Us</span>
    </nav>
    <div class="social" aria-label="Social links"><span></span><span></span><span></span><span></span></div>
    <div class="copy">© 2015, www.veltharidgellc.com</div>
  </footer>

</div>
</body>
</html>
```